Professional modern business card design

A business card for my nutrition business, wanting a professional look, with info clearly visible. Open to using logo colours too.

Would like key info on the front -
logo
my name and qualifications
email
phone number

and just an enlarged logo again / image on the back.

```html
<!DOCTYPE html>
<html lang="en">
<head>
<meta charset="UTF-8">
<title>Orla Nutrition – Business Card</title>
<link rel="stylesheet" href="https://fonts.googleapis.com/css2?family=Arimo:wght@400;700&display=swap">
<style>
  :root {
    --lime: #d4e021;
    --lime-deep: #bcc81a;
    --ink: #2e2e2e;
    --grey: #6a6a6a;
    --rule: #8a8a8a;
    --paper: #ffffff;
    --backdrop: #e9e9e9;
  }
  * { margin: 0; padding: 0; box-sizing: border-box; }
  html, body { width: 1200px; height: 802px; overflow: hidden; }
  body {
    background: var(--backdrop);
    display: flex;
    align-items: center;
    justify-content: center;
    gap: 40px;
    font-family: "Arimo", sans-serif;
  }
  .card {
    width: 540px;
    height: 309px;
    position: relative;
    box-shadow: 0 10px 30px rgba(0,0,0,0.12);
  }
  .card--front {
    background: var(--paper);
    border-bottom: 4px solid var(--lime);
    border-left: 4px solid var(--lime);
    display: flex;
    align-items: center;
    padding: 0 30px 0 40px;
  }
  .brand {
    display: flex;
    align-items: center;
    gap: 10px;
  }
  .brand__mark {
    width: 14px;
    height: 14px;
    background: var(--lime);
    flex: none;
  }
  .brand__name {
    font-family: "Arimo", sans-serif;
    font-weight: 700;
    color: var(--ink);
    white-space: nowrap;
  }
  .card--front .brand { width: 208px; margin-top: 110px; }
  .card--front .brand__name { font-size: 24px; }
  .divider {
    width: 1px;
    align-self: stretch;
    margin: 70px 26px 60px 10px;
    background: var(--rule);
  }
  .contact {
    color: var(--grey);
    font-size: 13px;
    line-height: 1.35;
    margin-bottom: 20px;
  }
  .contact__name {
    color: var(--lime);
    font-size: 17px;
    letter-spacing: 0.5px;
    text-transform: uppercase;
  }
  .contact__role { margin-bottom: 12px; }
  .contact__address { margin-bottom: 12px; }
  .contact__line { display: flex; align-items: center; gap: 7px; white-space: nowrap; }
  .contact__line svg { width: 11px; height: 11px; flex: none; }
  .card--back {
    background: var(--lime);
    display: flex;
    align-items: center;
    justify-content: center;
  }
  .card--back .brand__name {
    font-size: 50px;
    color: var(--lime-deep);
  }
  .card--back .brand__mark {
    width: 26px;
    height: 26px;
    background: var(--lime-deep);
  }
  .card--back .brand { gap: 16px; }
</style>
</head>
<body>
  <section class="card card--front">
    <div class="brand">
      <span class="brand__mark"></span>
      <span class="brand__name">Orla Nutrition</span>
    </div>
    <div class="divider"></div>
    <div class="contact">
      <p class="contact__name">Marcus Hale</p>
      <p class="contact__role">Manager</p>
      <p class="contact__address">Your Address, City<br>State, Zip 0000</p>
      <p class="contact__line">
        <svg viewBox="0 0 12 12"><path fill="#d4e021" d="M2.5 1h2l1 3-1.3 1a7 7 0 0 0 2.8 2.8L8 6.5l3 1v2A1.5 1.5 0 0 1 9.5 11 8.5 8.5 0 0 1 1 2.5 1.5 1.5 0 0 1 2.5 1z"/></svg>
        555-014-2283
      </p>
      <p class="contact__line">
        <svg viewBox="0 0 12 12"><rect x="0.5" y="2" width="11" height="8" fill="#d4e021"/><path d="M0.8 2.4 6 6.6l5.2-4.2" fill="none" stroke="#fff" stroke-width="1"/></svg>
        marcus@orlanutrition.com
      </p>
      <p class="contact__line">
        <svg viewBox="0 0 12 12"><circle cx="6" cy="6" r="5.5" fill="#d4e021"/><circle cx="6" cy="6" r="2" fill="#fff"/></svg>
        www.orlanutrition.com
      </p>
    </div>
  </section>

  <section class="card card--back">
    <div class="brand">
      <span class="brand__mark"></span>
      <span class="brand__name">Orla Nutrition</span>
    </div>
  </section>
</body>
</html>
```